Rosa Caring Star registered NDIS provider

Quality Care, Endless Support: Your NDIS Journey Starts Here
Rosa Caring Star is a compassionate Disability Support Service based in Liverpool NSW . We will provide you and your loved ones professional care and support that is tailored to your individual needs. We offer approved specialised short to long term disability accommodations, support independent living (SIL), assistance with daily tasks including cleaning, meal preparation and gardening, as well as daily programs and activities that range from personal training, community outings, videogames, table tennis, arts and craft, movies, and so much more!
To learn more about our services, feel free to browse our website to read about our NDIS-related blogs. For more information, get in touch with our friendly staff.
Work with Rosa Caring Star today. You and your loved ones deserve only the best.

ROSA CARING STAR
registered NDIS provider
Our services:
Approved specialised disability accommodations.

Support independent living SIL.

Short term accommodations/tenancy & respite.

Development of daily living & life skills

Overnight care active/non-active

Group/day centre activities

Assist in personal care.

Participation in community

Social and civic activities

Daily personal activities

Household tasks

Lawn mowing

Lifelong learning

Daily activities

Meal preparations

Support coordination

Plan management

Registered NDIS Provider
address 47 Brindle Crescent Liverpool NSW 2170
Phone : 0293416578/0471593824
Email : info@rosacaring.example.com.au
Web: : www.rosacaring.example.com.au
our servises in arabic
الخدمات تشمل
١- مساعدة التنقل .

٢- المشاركة الاجتماعية .

٣- تنمية المهارات الحياتية .

٤- مساعدة الأنشطة الشخصية .

٥- المساعدة في المهام المنزلية .

٦- مبيت (Respite ) وعناية على مدار ٢٤ ساعة .

٧- تطوير كافة المهارات اليومية مثلا تعلم الطبخ والميكاب تطوير المهارات الاجتماعية والحياة اليومية و طرق التنقل الامن مثل الباص و القطار
٨- العناية الشخصية والجسدية .
بإلاضافة الى السفرات الفردية والجماعية لمختلف الاعمار .

٩- بيوت مجهزة للسكن الدائمي لخدمات ذوي الاحتياجات الخاصه مع رعايه على مدار ٢٤ ساعة .

Target Market(s)

Disabilty people they need services from ndis provider which is my company registered company with ndis

Industry/Entity Type

Ndis disability services

Font styles to use
Serif

Colors
59FF00
82FF00
B8FF75
E3FFCB
F4FFEA
A7469A
B969AE
D3A5CF
EDDBEB
F8F0F9

Requirements
Must have
• Ndis logo and nice pictures for peoples with disability age from 9 years to 65 years
Should not have
• Old people

```html
<!DOCTYPE html>
<html lang="en">
<head>
<meta charset="utf-8">
<title>Rosa Caring Star – Registered NDIS Service Provider</title>
<link href="https://fonts.googleapis.com/css2?family=Poppins:wght@400;500;600;700&display=swap" rel="stylesheet">
<style>
  :root{
    --green:#72bf44;
    --green-soft:#86c962;
    --purple:#a0409a;
    --ink:#1f1f1f;
    --paper:#f7f7f7;
    --white:#ffffff;
    --sky:#ece9e1;
    --haze:#c9c8bf;
    --city:#a3a9a0;
  }
  *{box-sizing:border-box;margin:0;padding:0}
  html,body{width:972px;height:1200px;overflow:hidden}
  body{font-family:'Poppins',sans-serif;color:var(--ink);background:var(--paper)}
  .flyer{position:relative;width:972px;height:1200px;overflow:hidden;
    background:radial-gradient(ellipse at 20% 10%,#e9e9e9 0%,#f6f6f6 40%,#ffffff 75%);}

  .brand{position:absolute;left:170px;top:180px;display:flex;align-items:center;gap:26px}
  .brand-dot{width:50px;height:50px;border-radius:50%;background:var(--green)}
  .brand-name{font-weight:700;font-size:28px;line-height:29px;color:var(--ink);letter-spacing:.2px}

  .headline{position:absolute;left:401px;top:39px;width:528px;height:129px;background:var(--green);
    color:var(--white);padding:12px 0 0 15px}
  .headline h1{font-weight:600;font-size:53px;line-height:50px;letter-spacing:-1.8px;text-transform:uppercase}

  .intro{position:absolute;left:401px;top:168px;width:528px;height:91px;background:var(--purple);
    color:var(--white);padding:18px 10px 0 16px;font-size:20px;line-height:27px;font-weight:500;letter-spacing:-.3px}

  .hero{position:absolute;left:42px;top:276px;width:886px;height:309px;
    background:
      radial-gradient(ellipse at 62% 8%,rgba(255,252,240,.9) 0%,rgba(255,252,240,0) 45%),
      linear-gradient(180deg,var(--sky) 0%,var(--haze) 18%,var(--city) 32%,#93ad86 48%,var(--green-soft) 68%,var(--green) 100%)}
  .hero h2{position:absolute;left:22px;bottom:12px;color:var(--white);font-weight:600;font-size:39px;line-height:1;letter-spacing:-1px}

  .services{list-style:none}
  .service{position:absolute;transform:translateY(-50%);font-size:18.5px;line-height:23px;letter-spacing:-.2px}
  .service.left{left:105px}
  .service.right{left:608px}
  .service svg{position:absolute;left:-52px;top:50%;transform:translateY(-50%);width:32px;height:32px;fill:none;stroke-width:1.5}
  .service.left svg{stroke:var(--purple)}
  .service.right svg{stroke:var(--green)}

  .footer{position:absolute;left:0;top:1075px;width:972px;height:125px;background:var(--purple);color:var(--white)}
  .address{position:absolute;left:105px;top:24px;font-style:normal;font-weight:600;font-size:22px;line-height:26px;letter-spacing:-.4px}
  .contact{position:absolute;left:585px;top:26px;list-style:none;font-weight:500;font-size:18.5px;line-height:28px}
  .footer svg{position:absolute;fill:var(--white)}
</style>
</head>
<body>
<main class="flyer">
  <div class="brand">
    <span class="brand-dot"></span>
    <div class="brand-name">ROSA<br>CARING<br>STAR</div>
  </div>

  <header class="headline"><h1>Registered NDIS<br>Service Provider</h1></header>
  <p class="intro">Rosa Caring Star is an NDIS disability service provider based in Liverpool Sydney.</p>

  <section class="hero" role="img" aria-label="Photo of two young people in wheelchairs holding hands by a waterfront railing at sunset with a city skyline">
    <h2>OUR SERVICES</h2>
  </section>

  <ul class="services">
    <li class="service left" style="top:646px">
      <svg viewBox="0 0 30 30"><path d="M15 3 28 27H2Z M15 11 22 23H8Z"/></svg>
      <span>Approved specialised disability<br>accommodations.</span></li>
    <li class="service left" style="top:707px">
      <svg viewBox="0 0 30 30"><circle cx="15" cy="12" r="9"/><path d="M6 12h18M15 3v18M4 20l6 7M26 20l-6 7"/></svg>
      <span>Support independent living SIL.</span></li>
    <li class="service left" style="top:769px">
      <svg viewBox="0 0 30 30"><path d="M15 3 25 7v8c0 6-5 10-10 12C10 25 5 21 5 15V7Z"/><circle cx="15" cy="15" r="4"/></svg>
      <span>Short term accommodations/<br>tenancy &amp; respite.</span></li>
    <li class="service left" style="top:831px">
      <svg viewBox="0 0 30 30"><path d="M8 27v-6C4 18 4 12 7 8s10-6 15-2 4 10 2 12v3h-4v6"/><path d="M11 13l3 3 5-5"/></svg>
      <span>Development of daily living &amp; life skills</span></li>
    <li class="service left" style="top:881px">
      <svg viewBox="0 0 30 30"><path d="M15 12c-2-4-7-2-5 2l5 4 5-4c2-4-3-6-5-2Z M3 10l5 14h5 M27 10l-5 14h-5"/></svg>
      <span>Overnight care active/non-active</span></li>
    <li class="service left" style="top:930px">
      <svg viewBox="0 0 30 30"><rect x="8" y="3" width="14" height="8" rx="2"/><circle cx="6" cy="18" r="2.5"/><circle cx="15" cy="18" r="2.5"/><circle cx="24" cy="18" r="2.5"/><path d="M2 27c0-4 8-4 8 0M11 27c0-4 8-4 8 0M20 27c0-4 8-4 8 0"/></svg>
      <span>Group/day centre activities</span></li>
    <li class="service left" style="top:980px">
      <svg viewBox="0 0 30 30"><circle cx="10" cy="9" r="3"/><circle cx="21" cy="9" r="3"/><path d="M6 28V15h8v13M17 28V15h8v13"/></svg>
      <span>Assist in personal care.</span></li>
    <li class="service left" style="top:1030px">
      <svg viewBox="0 0 30 30"><circle cx="9" cy="6" r="2.5"/><circle cx="15" cy="6" r="2.5"/><circle cx="21" cy="6" r="2.5"/><path d="M3 12l6 15h4 M27 12l-6 15h-4 M15 13v10"/></svg>
      <span>Participation in community</span></li>

    <li class="service right" style="top:635px">
      <svg viewBox="0 0 30 30"><circle cx="13" cy="9" r="5"/><path d="M4 27c0-7 5-10 9-10"/><circle cx="21" cy="21" r="5"/><path d="M19 21l2 2 3-4"/></svg>
      <span>Social and civic activities</span></li>
    <li class="service right" style="top:685px">
      <svg viewBox="0 0 30 30"><circle cx="13" cy="8" r="5"/><path d="M3 27v-4c0-4 4-6 10-6"/><circle cx="22" cy="22" r="5"/><path d="M20 22l2 2 3-4"/></svg>
      <span>Daily personal activities</span></li>
    <li class="service right" style="top:735px">
      <svg viewBox="0 0 30 30"><path d="M3 14 15 4l12 10M6 12v15h18V12"/><rect x="12" y="19" width="6" height="8"/></svg>
      <span>Household tasks</span></li>
    <li class="service right" style="top:785px">
      <svg viewBox="0 0 30 30"><path d="M2 28h26M4 24h12v-4H6ZM16 20l8-14"/><circle cx="7" cy="25" r="2"/><circle cx="14" cy="25" r="2"/></svg>
      <span>Lawn mowing</span></li>
    <li class="service right" style="top:835px">
      <svg viewBox="0 0 30 30"><path d="M14 4c-6 0-10 4-10 9s3 7 4 9v5h6V4M16 10h8M16 16h10M16 22h7"/></svg>
      <span>Lifelong learning</span></li>
    <li class="service right" style="top:885px">
      <svg viewBox="0 0 30 30"><rect x="4" y="6" width="22" height="21" rx="2"/><path d="M4 11h22M9 3v5M21 3v5"/><circle cx="15" cy="19" r="4"/><path d="M13 19l2 2 3-3"/></svg>
      <span>Daily activities</span></li>
    <li class="service right" style="top:935px">
      <svg viewBox="0 0 30 30"><circle cx="15" cy="15" r="8"/><circle cx="15" cy="15" r="4"/><path d="M3 5v20M27 5v20"/></svg>
      <span>Meal preparations</span></li>
    <li class="service right" style="top:985px">
      <svg viewBox="0 0 30 30"><path d="M4 20l8-8 4 3 4-4 6 6-8 8-4-2-4 3Z M15 3v3M9 5l2 2M21 5l-2 2"/></svg>
      <span>Support coordination</span></li>
    <li class="service right" style="top:1035px">
      <svg viewBox="0 0 30 30"><path d="M9 27v-6C5 18 5 12 8 8s10-6 14-2 4 10 1 13v8"/><circle cx="15" cy="14" r="3"/></svg>
      <span>Plan management</span></li>
  </ul>

  <footer class="footer">
    <svg viewBox="0 0 24 24" width="24" height="24" style="left:64px;top:28px" aria-hidden="true"><path d="M12 2a7 7 0 0 0-7 7c0 5 7 13 7 13s7-8 7-13a7 7 0 0 0-7-7Zm0 10a3 3 0 1 1 0-6 3 3 0 0 1 0 6Z"/></svg>
    <address class="address">47 Brindle Crescent<br>Liverpool NSW 2170</address>

    <svg viewBox="0 0 24 24" width="20" height="20" style="left:546px;top:30px" aria-hidden="true"><path d="M6.6 10.8a15 15 0 0 0 6.6 6.6l2.2-2.2c.3-.3.7-.4 1-.2 1.1.4 2.3.6 3.6.6.6 0 1 .4 1 1V20c0 .6-.4 1-1 1A17 17 0 0 1 3 4c0-.6.4-1 1-1h3.5c.6 0 1 .4 1 1 0 1.3.2 2.5.6 3.6.1.3 0 .7-.2 1Z"/></svg>
    <svg viewBox="0 0 24 24" width="20" height="20" style="left:546px;top:58px" aria-hidden="true"><path d="M2 5h20v14H2Zm1 1 9 7 9-7Z"/></svg>
    <svg viewBox="0 0 24 24" width="18" height="18" style="left:548px;top:87px" aria-hidden="true"><path d="M4 2 20 12l-7 1 4 8-3 1-4-8-5 5Z"/></svg>
    <ul class="contact">
      <li>0293416578/0471593824</li>
      <li>info@rosacaring.example.com.au</li>
      <li>www.rosacaring.example.com.au</li>
    </ul>
  </footer>
</main>
</body>
</html>
```